SUMMIT GATHERING 2021. August 20th -22nd.

The Hosts of the conference: Grace Tabernacle-Pastors Ron n Molly ( Picture with two persons)

Guest Minister: Bishop Lorna Kiprotich. (Cedar Ridge Evangelist)

Venue:
Seattle Harborgate Lodge. 4817 North 92nd Avenue Seattle, WA 98134.

Conference times.
Friday August 20th 6pm-8:30pm
Saturday August 21st. 6pm-8:30pm

Sunday August 22nd 10am-1pm
“ CHURCH RENEWAL SERVICE”

5pm-7:30pm
TWOFOLD BLESSING SERVICE.

Target Market(s)

18-55

Industry/Entity Type

Religious/ Entertainment.

Requirements
Must have
• A highlight of the Relaunch service on Sunday August 22nd 5pm-7:30pm.
Nice to have
• Excellent ideas….

```html
<!DOCTYPE html>
<html lang="en">
<head>
<meta charset="utf-8">
<title>Summit Gathering 2021</title>
<link rel="stylesheet" href="https://fonts.googleapis.com/css2?family=Montserrat:ital,wght@0,300;0,400;0,500;0,700;1,400&family=Great+Vibes&family=Roboto+Condensed:wght@400;700&display=swap">
<style>
:root{
  --bg-deep:#020406;
  --bg-navy:#0b2a40;
  --bg-swoosh:#123a57;
  --orange:#f26a12;
  --cyan:#35c6e8;
  --white:#ffffff;
  --soft:#e9eef2;
  --gold:#c9a04a;
  --photo-a:#3a2a22;
  --photo-b:#7a7f86;
}
*{margin:0;padding:0;box-sizing:border-box}
html,body{width:1200px;height:800px;overflow:hidden;background:var(--bg-deep)}
.flyer{position:relative;width:1200px;height:800px;overflow:hidden;
  background:radial-gradient(ellipse at 65% 85%,var(--bg-navy) 0%,#061522 55%,var(--bg-deep) 100%);
  font-family:'Montserrat',sans-serif;color:var(--white)}
.swoosh{position:absolute;inset:0}
.brand{position:absolute;left:55px;top:52px;width:135px;height:162px;
  display:flex;flex-direction:column;align-items:center;justify-content:center;gap:12px;
  background:#0d0d0d;border:1px solid #2a2a2a}
.brand-mark{width:26px;height:26px;background:var(--gold)}
.brand-name{font-family:'Montserrat',sans-serif;font-weight:700;font-size:15px;color:var(--gold);
  text-align:center;line-height:1.2;text-transform:uppercase}
.title{position:absolute;left:316px;top:40px;font-weight:700;color:var(--orange);
  font-size:104px;line-height:94px;letter-spacing:1px}
.year{position:absolute;right:62px;top:58px;font-weight:400;font-size:90px;color:var(--white)}
.speaker-photo{position:absolute;left:0;top:227px;width:462px;height:573px;
  background:linear-gradient(180deg,var(--photo-a) 0%,#5b4a44 45%,var(--photo-b) 100%);
  border-top-right-radius:200px 260px}
.service-label{position:absolute;top:310px;font-family:'Great Vibes',cursive;font-size:32px;color:var(--white)}
.label-renewal{left:398px}
.label-twofold{left:760px}
.day{position:absolute;top:352px;text-align:center;width:220px}
.day-name{font-weight:500;font-size:27px;color:var(--cyan);letter-spacing:1px;line-height:34px}
.day-date{font-weight:500;font-size:25px;color:var(--orange);line-height:30px}
.day-times{font-weight:300;font-size:28px;line-height:34px;margin-top:2px}
.day-fri{left:427px}
.day-sat{left:663px}
.day-sun{left:882px;width:260px}
.day-sat .day-times,.day-sun .day-times{margin-top:-4px}
.sun-times{display:grid;grid-template-columns:1fr 1fr;column-gap:16px}
.venue{position:absolute;left:400px;top:494px;width:740px;text-align:center}
.venue-label{font-style:italic;font-size:20px;line-height:26px}
.venue-address{font-size:19px;line-height:26px;margin-top:6px}
.guest{position:absolute;left:450px;top:604px;width:480px;text-align:center}
.guest-label{font-family:'Great Vibes',cursive;font-size:48px;line-height:56px}
.guest-name{font-family:'Roboto Condensed',sans-serif;font-weight:700;font-size:37px;line-height:42px;margin-top:-2px}
.guest-title{font-family:'Roboto Condensed',sans-serif;font-size:29px;line-height:34px;color:var(--soft)}
.host-photo{position:absolute;left:994px;top:576px;width:146px;height:164px;
  border:3px solid var(--orange);
  background:linear-gradient(160deg,#f4f4f4 0%,#6b4a3a 55%,#2b1d18 100%)}
.host-credit{position:absolute;left:955px;top:750px;font-family:'Roboto Condensed',sans-serif;
  font-weight:700;font-size:17px;white-space:nowrap}
</style>
</head>
<body>
<main class="flyer">
  <svg class="swoosh" width="1200" height="800" viewBox="0 0 1200 800" aria-hidden="true">
    <defs>
      <linearGradient id="swooshFill" x1="0" y1="0" x2="1" y2="0">
        <stop offset="0" stop-color="#0a2233" stop-opacity="0.2"/>
        <stop offset="0.6" stop-color="#123a57" stop-opacity="0.9"/>
        <stop offset="1" stop-color="#1a4a6c"/>
      </linearGradient>
    </defs>
    <path d="M0 400 C250 250 650 160 1200 40 L1200 110 C760 190 380 300 60 470 Z" fill="url(#swooshFill)"/>
    <path d="M20 470 C360 300 760 200 1200 110 L1200 800 L0 800 Z" fill="#071a29" opacity="0.55"/>
  </svg>

  <div class="brand">
    <span class="brand-mark"></span>
    <span class="brand-name">Grace<br>Tabernacle</span>
  </div>

  <h1 class="title">SUMMIT<br>GATHERING</h1>
  <div class="year">2021</div>

  <div class="speaker-photo" role="img" aria-label="Portrait photo of guest speaker Bishop Lorna Kiprotich"></div>

  <div class="service-label label-renewal">Church Renewal Service</div>
  <div class="service-label label-twofold">Twofold Blessing Service</div>

  <section class="day day-fri">
    <div class="day-name">FRIDAY</div>
    <div class="day-date">AUGUST 20th</div>
    <div class="day-times">6:00PM<br>8:30PM</div>
  </section>
  <section class="day day-sat">
    <div class="day-name">SATURDAY</div>
    <div class="day-date">AUGUST 21st</div>
    <div class="day-times">6:00PM<br>8:30PM</div>
  </section>
  <section class="day day-sun">
    <div class="day-name">SUNDAY</div>
    <div class="day-date">AUGUST 22nd</div>
    <div class="day-times sun-times"><span>10:00AM</span><span>5:00PM</span><span>1:00PM</span><span>7:30PM</span></div>
  </section>

  <section class="venue">
    <div class="venue-label">Conference Venue</div>
    <div class="venue-address">Seattle Harborgate Lodge. 4817 North 92nd Avenue&nbsp; Seattle, WA 98134.</div>
  </section>

  <section class="guest">
    <div class="guest-label">Guest Speaker</div>
    <div class="guest-name">Bishop Lorna Kiprotich</div>
    <div class="guest-title">(Cedar Ridge Evangelist)</div>
  </section>

  <div class="host-photo" role="img" aria-label="Photo of hosts Pastors Ron and Molly"></div>
  <div class="host-credit">Host:&nbsp; Pastors Ron &amp; Molly</div>
</main>
</body>
</html>
```